Flyer for language school

Hi,
We are language school, we offre german courses.
We will provide our students with a notepad during registration in a german course.
For that, we need the front page ofthe notepad to be pretty, simple and remarkable.
U can find our colors in the logo in the attachement.
for the contact information, we need those three adresses
Tunis - Imm Les Cyprès, 3ème étage 47 Rue des Palmiers Bleus, 1053 Les Berges du Lac 1
Tél : 71 482 613
Email : tunis@vorlinda.org
Sfax - Imm Zahrat, 5ème étage Rue Slim Bouraoui (en face de la crvp), 3027 Sfax
Tél : 74 613 952
Email : sfax@vorlinda.org
Sousse - 54 Ave Tahar Kelibi (prés du rond point Belvista au dessus du café Myrtille).
Tél : 73 590 126
Email : sousse@vorlinda.org
The website needs to be cited also :
www.vorlinda.org
School

```html
<!DOCTYPE html>
<html lang="fr">
<head>
<meta charset="utf-8">
<title>Vorlinda – Lerne Deutsch mit uns</title>
<link rel="stylesheet" href="https://fonts.googleapis.com/css2?family=Permanent+Marker&family=Arimo:wght@400;700&display=swap">
<style>
  :root {
    --backdrop: #dcdcdc;
    --cover-light: #ffffff;
    --cover-shade: #e4e4e4;
    --ink: #161616;
    --lime: #c3cf28;
    --lime-dark: #9aa51c;
    --lime-fold: #7e8716;
    --text-grey: #6e6e6e;
    --text-dark: #4a4a4a;
    --rule: #c9c9c9;
    --marker: "Permanent Marker", "Comic Sans MS", "Chalkboard SE", sans-serif;
  }
  * { box-sizing: border-box; margin: 0; padding: 0; }
  html, body { width: 1200px; height: 960px; overflow: hidden; }
  body {
    background: var(--backdrop);
    font-family: "Arimo", Arial, sans-serif;
    position: relative;
  }
  .cover {
    position: absolute;
    left: 300px; top: 40px;
    width: 600px; height: 880px;
    background: radial-gradient(ellipse at 55% 55%, var(--cover-light) 0%, #f4f4f4 55%, var(--cover-shade) 100%);
    box-shadow: 0 6px 24px rgba(0,0,0,.18);
    overflow: hidden;
  }
  .headline {
    position: absolute;
    left: 40px; top: 70px;
    width: 370px;
    font-family: var(--marker);
    font-weight: 700;
    font-size: 54px;
    line-height: 1.05;
    color: var(--ink);
    text-align: center;
    transform: rotate(-3deg);
    letter-spacing: 3px;
  }
  .headline span { display: block; }
  .hand-photo {
    position: absolute;
    left: 455px; top: 205px;
    width: 145px; height: 95px;
    background: linear-gradient(160deg, #c8ccd4 0%, #9ea4ae 60%, #e2c7b5 100%);
    border-radius: 48px 0 0 36px;
  }
  .banner {
    position: absolute;
    left: 70px; top: 420px;
    width: 480px; height: 190px;
  }
  .banner-text {
    font-family: var(--marker);
    font-weight: 700;
    font-size: 28px;
    fill: #ffffff;
    letter-spacing: 1px;
  }
  .brand {
    position: absolute;
    left: 320px; top: 575px;
    display: flex; align-items: center; gap: 10px;
  }
  .brand-dot {
    width: 34px; height: 34px; border-radius: 50%;
    background: var(--lime);
  }
  .brand-name {
    font-weight: 700; font-size: 34px; color: var(--ink);
  }
  .website {
    position: absolute;
    left: 0; right: 0; top: 680px;
    text-align: center;
    font-size: 13px; font-weight: 700;
    letter-spacing: 9px; color: var(--text-dark);
  }
  .offices {
    position: absolute;
    left: 30px; right: 30px; top: 718px;
    display: grid; grid-template-columns: 1fr 1fr 1fr;
    border-top: 1px solid var(--rule);
    padding-top: 14px;
  }
  .office {
    padding: 0 12px;
    font-size: 10.5px; line-height: 1.35; color: var(--text-grey);
  }
  .office + .office { border-left: 1px dotted var(--rule); }
  .office-city { font-size: 14px; font-weight: 700; color: var(--text-dark); margin-bottom: 3px; }
  .office-address { margin-bottom: 6px; }
  .contact { display: flex; align-items: center; gap: 5px; }
  .contact svg { width: 13px; height: 13px; flex: none; }
  .social {
    display: flex; align-items: center; gap: 5px;
    margin-top: 8px; font-size: 13px; color: #8a8a8a; letter-spacing: 1px;
  }
  .social-square { width: 13px; height: 13px; background: #7f93b8; }
</style>
</head>
<body>
  <main class="cover">
    <h1 class="headline"><span>SPRICHST</span><span>DU</span><span>DEUTSCH?</span></h1>

    <div class="hand-photo" role="img" aria-label="Photo of a hand in a grey shirt sleeve holding a marker, writing the headline"></div>

    <svg class="banner" viewBox="0 0 480 190" aria-label="Lerne Deutsch mit uns!">
      <polygon points="95,120 175,108 150,185" fill="var(--lime-fold)"/>
      <polygon points="95,120 150,185 120,150" fill="var(--lime-dark)"/>
      <g transform="rotate(-11 240 80)">
        <rect x="20" y="55" width="450" height="52" fill="var(--lime)"/>
        <text class="banner-text" x="245" y="92" text-anchor="middle">LERNE DEUTSCH MIT UNS!</text>
      </g>
    </svg>

    <div class="brand">
      <span class="brand-dot"></span>
      <span class="brand-name">vorlinda</span>
    </div>

    <p class="website">www.vorlinda.org</p>

    <section class="offices">
      <article class="office">
        <h2 class="office-city">Tunis</h2>
        <p class="office-address">Imm Les Cyprès, 3ème étage 47 Rue des Palmiers Bleus, 1053 Les Berges du Lac 1</p>
        <p class="contact">
          <svg viewBox="0 0 14 14"><rect width="14" height="14" rx="2" fill="var(--lime)"/><path d="M4 3.5c0 4 2.5 6.5 6.5 6.5l.5-1.8-2-.8-.8 1c-1.3-.5-2.3-1.5-2.8-2.8l1-.8-.8-2z" fill="var(--ink)"/></svg>
          Tél : 71 482 613
        </p>
        <p class="contact">
          <svg viewBox="0 0 14 14"><rect width="14" height="14" rx="2" fill="var(--lime)"/><circle cx="7" cy="7" r="4" fill="var(--ink)"/></svg>
          Email : tunis@vorlinda.org
        </p>
        <p class="social"><span class="social-square"></span>VORLINDA</p>
      </article>
      <article class="office">
        <h2 class="office-city">Sfax</h2>
        <p class="office-address">Imm Zahrat, 5ème étage Rue Slim Bouraoui (en face de la crvp), 3027 Sfax</p>
        <p class="contact">
          <svg viewBox="0 0 14 14"><rect width="14" height="14" rx="2" fill="var(--lime)"/><path d="M4 3.5c0 4 2.5 6.5 6.5 6.5l.5-1.8-2-.8-.8 1c-1.3-.5-2.3-1.5-2.8-2.8l1-.8-.8-2z" fill="var(--ink)"/></svg>
          Tél : 74 613 952
        </p>
        <p class="contact">
          <svg viewBox="0 0 14 14"><rect width="14" height="14" rx="2" fill="var(--lime)"/><circle cx="7" cy="7" r="4" fill="var(--ink)"/></svg>
          Email : sfax@vorlinda.org
        </p>
      </article>
      <article class="office">
        <h2 class="office-city">Sousse</h2>
        <p class="office-address">54 Ave Tahar Kelibi (prés du rond point Belvista au dessus du café Myrtille)</p>
        <p class="contact">
          <svg viewBox="0 0 14 14"><rect width="14" height="14" rx="2" fill="var(--lime)"/><path d="M4 3.5c0 4 2.5 6.5 6.5 6.5l.5-1.8-2-.8-.8 1c-1.3-.5-2.3-1.5-2.8-2.8l1-.8-.8-2z" fill="var(--ink)"/></svg>
          Tél : 73 590 126
        </p>
        <p class="contact">
          <svg viewBox="0 0 14 14"><rect width="14" height="14" rx="2" fill="var(--lime)"/><circle cx="7" cy="7" r="4" fill="var(--ink)"/></svg>
          Email : sousse@vorlinda.org
        </p>
      </article>
    </section>
  </main>
</body>
</html>
```